Lose Up To 1 LB Of Fat Per Day

We need a double sided street sign for our weight loss clinic. We need the doctors picture to the right side of the sign and we need a challenge “Lose Up To 1 Pound Of Fat Per Day” included in the signage.
Our color scheme for the clinic are black, white, teal and silver.
The phone number should be at the bottom of the sign
517-294–6038

Target Market(s)

Weight Loss

Font styles to use
Sans Serif

```html
<!DOCTYPE html>
<html lang="en">
<head>
<meta charset="utf-8">
<title>Weight Loss Clinic – Street Sign</title>
<link href="https://fonts.googleapis.com/css2?family=Lexend:wght@400;600;700&display=swap" rel="stylesheet">
<style>
  :root {
    --teal: #0f7f7b;
    --teal-glow: #4fa89c;
    --charcoal: #1f2226;
    --silver: #a9b1b6;
    --silver-light: #d4d9dc;
    --white: #ffffff;
    --page: #eceeee;
    --suit-dark: #1c1c20;
    --suit-mid: #3a3b42;
  }
  html, body {
    margin: 0;
    padding: 0;
    width: 833px;
    height: 1200px;
    overflow: hidden;
    background: var(--page);
  }
  .canvas {
    position: relative;
    width: 833px;
    height: 1200px;
    overflow: hidden;
  }
  .sign {
    position: absolute;
    left: 0;
    top: 288px;
    width: 1339px;
    height: 1003px;
    transform: scale(0.6221);
    transform-origin: 0 0;
    overflow: hidden;
    background:
      radial-gradient(circle at 1109px 300px, var(--teal-glow) 0, var(--teal) 300px);
    font-family: "Lexend", sans-serif;
    color: var(--white);
  }
  .sign-shapes {
    position: absolute;
    inset: 0;
  }
  .doctor-photo {
    position: absolute;
    left: 819px;
    top: 170px;
    width: 520px;
    height: 833px;
    border-radius: 200px 200px 0 0;
    background: linear-gradient(180deg, var(--teal-glow) 0%, var(--suit-mid) 40%, var(--suit-dark) 100%);
  }
  .challenge {
    position: absolute;
    left: 205px;
    top: 190px;
    margin: 0;
    font-weight: 700;
    font-size: 86px;
    line-height: 98px;
    letter-spacing: 1px;
  }
  .clinic-name {
    position: absolute;
    left: 85px;
    top: 760px;
    margin: 0;
    font-weight: 400;
    font-size: 76px;
    line-height: 90px;
    letter-spacing: 1px;
  }
  .phone {
    position: absolute;
    left: 85px;
    top: 848px;
    margin: 0;
    font-weight: 700;
    font-size: 86px;
    line-height: 96px;
  }
</style>
</head>
<body>
<main class="canvas">
  <section class="sign">
    <svg class="sign-shapes" width="1339" height="1003" viewBox="0 0 1339 1003" aria-hidden="true">
      <polygon points="260,30 790,235 595,755 65,560" fill="var(--silver)"/>
      <polygon points="210,55 770,190 635,735 85,600" fill="var(--charcoal)"/>
      <g stroke="var(--silver-light)" stroke-width="4" stroke-linecap="round">
        <line x1="45" y1="145" x2="340" y2="145"/>
        <line x1="142" y1="175" x2="272" y2="175"/>
        <line x1="565" y1="618" x2="710" y2="618"/>
        <line x1="455" y1="648" x2="745" y2="648"/>
      </g>
    </svg>
    <div class="doctor-photo" role="img" aria-label="Portrait of the clinic doctor in a dark suit and white shirt"></div>
    <h1 class="challenge">Lose Up To<br>1 Pound<br>Of Fat<br>Per Day</h1>
    <p class="clinic-name">DR Lindqvist’</p>
    <p class="phone">517-294–6038</p>
  </section>
</main>
</body>
</html>
```